New Letterhead request for our Law Firm!

We are a small Estate Planning Firm who just got out logo redesigned. It's attached. We need some letterhead for our client welcome letters and so forth. Clean, bright, and approachable is our style. If you need the specifications for our color scheme or other versions of the logo file, we have those too. Visit our website to get an idea about our services/aesthetics:https://bramblecove.law/

Target Market(s)

Adults 30-80

Colors

Designer to choose colors to be used in the design.

Requirements
Must have
• Logo with color. Contact information

```html
<!DOCTYPE html>
<html lang="en">
<head>
<meta charset="utf-8">
<title>Bramblecove Law Firm Letterhead</title>
<link href="https://fonts.googleapis.com/css2?family=Zilla+Slab:wght@600&family=Lato:wght@400;700&display=swap" rel="stylesheet">
<style>
  :root {
    --backdrop: #cdc2bf;
    --paper: #fdfdf8;
    --sage: #6b9a80;
    --ink: #3a3b3d;
    --muted: #4a4b4d;
  }
  * { box-sizing: border-box; margin: 0; padding: 0; }
  html, body {
    width: 1200px; height: 784px; overflow: hidden;
    background: var(--backdrop);
  }
  .canvas {
    width: 1200px; height: 784px;
    display: flex; align-items: center; justify-content: center;
  }
  .letterhead {
    position: relative;
    width: 556px; height: 720px;
    background: var(--paper);
    box-shadow: 0 2px 10px rgba(0,0,0,0.12);
    overflow: hidden;
  }
  .brand {
    position: absolute; top: 38px; left: 40px;
    display: flex; align-items: center; gap: 12px;
  }
  .brand-circle {
    width: 52px; height: 52px; border-radius: 50%;
    border: 3px solid var(--sage);
    flex: none;
  }
  .brand-name {
    font-family: "Zilla Slab", Georgia, serif;
    font-weight: 600;
    color: var(--sage);
    font-size: 22px;
    letter-spacing: 0.06em;
    line-height: 1.1;
    text-transform: uppercase;
  }
  .contact {
    position: absolute; top: 40px; right: 34px;
    border-left: 1.5px solid var(--sage);
    padding-left: 10px;
    font-family: "Lato", Arial, sans-serif;
    font-size: 10px; line-height: 1.45;
    color: var(--muted);
  }
  .contact-firm { color: var(--sage); font-weight: 700; }
  .contact-row { display: flex; align-items: center; gap: 5px; }
  .contact-row svg { width: 9px; height: 9px; flex: none; }
  .contact-address { margin-bottom: 2px; }
  .footer-band {
    position: absolute; left: 0; bottom: 0;
    width: 100%; height: 26px;
  }
</style>
</head>
<body>
<main class="canvas">
  <article class="letterhead">
    <header class="brand">
      <span class="brand-circle" aria-hidden="true"></span>
      <span class="brand-name">Bramblecove<br>Law Firm</span>
    </header>

    <address class="contact">
      <div class="contact-firm">Bramblecove Law Firm, PLLC</div>
      <div class="contact-address">2410 Cedar Ridge Road, Suite 110<br>Fairhaven, MN 55990</div>
      <div class="contact-row">
        <svg viewBox="0 0 10 10" aria-hidden="true"><path d="M2 1l2 2-1 1.3c.6 1.2 1.5 2.1 2.7 2.7L7 6l2 2-1.3 1.3C4.6 9 1 5.4.7 2.3z" fill="var(--sage)"/></svg>
        <span>555-014-2276</span>
      </div>
      <div class="contact-row">
        <svg viewBox="0 0 10 10" aria-hidden="true"><rect x="0.5" y="2" width="9" height="6" fill="none" stroke="var(--sage)"/><path d="M.5 2L5 5.5 9.5 2" fill="none" stroke="var(--sage)"/></svg>
        <span>info@bramblecove.law</span>
      </div>
      <div class="contact-row">
        <svg viewBox="0 0 10 10" aria-hidden="true"><circle cx="5" cy="5" r="4.3" fill="none" stroke="var(--sage)"/><ellipse cx="5" cy="5" rx="1.8" ry="4.3" fill="none" stroke="var(--sage)"/><path d="M.7 5h8.6" stroke="var(--sage)"/></svg>
        <span>www.bramblecove.law</span>
      </div>
    </address>

    <svg class="footer-band" viewBox="0 0 556 26" preserveAspectRatio="none" aria-hidden="true">
      <polygon points="0,16 386,16 392,10 556,10 556,26 0,26" fill="var(--sage)"/>
      <polygon points="0,11 380,11 384,8 0,8" fill="var(--ink)"/>
      <polygon points="0,14 383,14 386,11 0,11" fill="var(--paper)"/>
    </svg>
  </article>
</main>
</body>
</html>
```